Virtual Reality medical education company

We are a new company that is offering virtual reality medical simulation suites. I have had a go at the initial web design www.corvandelhealthsim.example but as you can see I am no web designer!
I have the logo and some text which I'd like you to use - also some images. Any help with the SEO would be appreciated.

Target Market(s)

Students and faculty in medical and applied medical degrees

Industry/Entity Type

Education

Coding

Number of Pages Required

Font styles to use
Sans Serif

Requirements
Must have
• Home, Benefits, Simulation, Why Virtual, Modules, Contact Us
• Virtual reality scenes, either people using it or what they see.
• This is the patient we are using http://www.meshorbitly.example/3d-models/rigged-hospital-patient-3d-max/4827153
Nice to have
• Pelnor Drift or Zanthe Vista headsets being worn
Should not have
• Non VR simulation, real patients/models, students looking at computer screens

```html
<!DOCTYPE html>
<html lang="en">
<head>
<meta charset="utf-8">
<title>Corvandel Health Sim</title>
<link href="https://fonts.googleapis.com/css2?family=Cinzel:wght@400;600;700&family=Open+Sans:wght@400;600;700&display=swap" rel="stylesheet">
<style>
:root{
  --blue:#1b86d0;
  --blue-dark:#0f6fb6;
  --purple:#2e2a94;
  --purple-deep:#27238a;
  --ink:#1c1c1c;
  --text:#333;
  --muted:#666;
  --footer:#2e2e2e;
  --white:#fff;
  --red:#c9313b;
}
*{box-sizing:border-box;margin:0;padding:0}
html,body{width:1200px;height:3371px;overflow:hidden}
body{position:relative;background:var(--white);font-family:'Open Sans',sans-serif;color:var(--text)}
.abs{position:absolute}
.ph{position:absolute}

/* header */
.brand{left:55px;top:30px;display:flex;align-items:center;gap:12px}
.brand-mark{width:34px;height:34px;border-radius:50%;background:var(--blue)}
.brand-name{font-family:'Open Sans',sans-serif;font-weight:700;font-size:26px;color:var(--blue-dark);line-height:1.05;width:230px}
.top-social{right:60px;top:36px;display:flex;gap:7px}
.top-social span{width:22px;height:22px;background:var(--blue)}
.top-contact{right:60px;top:78px;font-size:13px;color:var(--ink);display:flex;gap:20px;align-items:center}
.top-contact svg{vertical-align:-2px;margin-right:4px}

.nav{left:0;top:120px;width:1200px;height:45px;background:var(--blue)}
.nav ul{list-style:none;display:flex;position:absolute;left:40px;top:0;height:45px}
.nav li{color:var(--white);font-weight:700;font-size:16px;padding:0 17px;line-height:45px;position:relative}
.nav li.active:after{content:"";position:absolute;left:17px;right:17px;bottom:6px;height:3px;background:var(--purple)}
.search{right:60px;top:6px;width:228px;height:33px;background:var(--white);border:1px solid #ccc;font-size:13px;color:#999;padding:7px 10px}
.search svg{position:absolute;right:8px;top:7px}

.hero{left:0;top:165px;width:1200px;height:443px;background:linear-gradient(100deg,#d9e3ec 0%,#aebfd0 35%,#6f94ba 60%,#2a5f99 100%)}
.hero-caption{left:680px;top:128px;width:460px;height:195px;background:rgba(40,40,45,.72);padding:26px 20px;color:var(--white)}
.hero-caption h1{font-family:'Cinzel',serif;font-weight:600;font-size:38px;letter-spacing:1px;line-height:1}
.hero-caption .sub{font-size:15px;margin-top:10px}
.hero-caption .rule{height:3px;background:var(--blue);width:290px;margin:8px 0 12px}
.hero-caption p{font-size:15px;line-height:1.5}
.dots{left:590px;top:408px;display:flex;gap:6px}
.dots span{width:11px;height:11px;border-radius:50%;background:var(--white)}
.dots span:first-child{background:#222}

/* welcome */
.welcome{left:55px;top:700px;width:610px}
.sec-title{font-family:'Cinzel',serif;font-weight:700;font-size:38px;color:var(--ink);line-height:1.1}
.sec-title em{font-style:normal;color:var(--purple)}
.welcome h3{font-size:17px;font-weight:700;color:var(--ink);margin:12px 0 22px}
.welcome p{font-size:13.5px;line-height:1.65;color:var(--text)}
.welcome h2{font-size:20px;font-weight:700;color:var(--ink);margin:18px 0 16px;display:flex;align-items:center;gap:10px}
.welcome h2:after{content:"";flex:1;height:2px;background:var(--ink)}
.btn-start{display:inline-block;margin-top:36px;background:var(--blue-dark);color:var(--white);font-weight:700;font-size:15px;padding:14px 18px;width:152px}
.clinic-card{left:770px;top:737px;width:370px;height:316px;background:var(--blue-dark)}
.clinic-card .ph{left:0;top:0;width:370px;height:232px;background:linear-gradient(180deg,#cfd6dc,#9aa7b2)}
.clinic-card .cap{position:absolute;top:240px;width:100%;text-align:center;color:var(--white);font-size:12.5px;line-height:1.5}
.clinic-card .more{position:absolute;left:150px;top:288px;width:70px;height:24px;background:var(--white);color:var(--ink);font-size:12px;font-weight:700;text-align:center;line-height:24px}

/* services */
.services{left:0;top:1175px;width:1200px;height:560px;background:var(--purple);clip-path:polygon(0 0,50% 14px,100% 0,100% 530px,50% 560px,0 530px)}
.services .sec-title{position:absolute;left:55px;top:70px;color:var(--white);font-size:34px}
.services .tag{position:absolute;left:58px;top:116px;color:var(--white);font-size:14px}
.svc{position:absolute;top:175px;width:213px;height:300px;background:var(--white);text-align:center}
.svc .ph{left:0;top:0;width:213px;height:157px}
.svc h4{position:absolute;top:170px;width:100%;font-size:17px;font-weight:700;color:var(--ink)}
.svc p{position:absolute;top:205px;left:15px;right:15px;font-size:12.5px;line-height:1.35;color:var(--text)}
.svc .rm{position:absolute;left:62px;bottom:-15px;width:87px;height:32px;background:var(--blue);color:var(--white);font-size:12px;font-weight:700;line-height:32px}
.other{position:absolute;left:782px;top:170px;width:320px;color:var(--white)}
.other h3{font-size:22px;font-weight:700}
.other p{font-size:13.5px;line-height:1.6;margin-top:12px}
.other .rm{margin-top:18px;width:316px;height:44px;background:var(--blue);font-size:14px;line-height:44px;padding-left:14px}

/* benefits */
.benefits-head{left:55px;top:1800px}
.benefits-head .sec-title{font-size:34px}
.benefits-head p{font-size:14px;color:var(--ink);margin-top:10px}
.ben{position:absolute;top:1915px;width:328px;height:410px;background:var(--purple)}
.ben .ph{left:0;top:0;width:328px;height:208px}
.ben h4{position:absolute;top:208px;width:100%;height:63px;background:var(--blue);color:var(--white);font-size:18px;font-weight:600;text-align:center;line-height:63px}
.ben p{position:absolute;top:288px;left:35px;right:35px;color:var(--white);font-size:13px;line-height:1.45;text-align:center}
.ben .rm{position:absolute;left:115px;top:355px;width:98px;height:42px;background:var(--white);color:var(--ink);font-weight:700;font-size:13px;text-align:center;line-height:42px}

/* cta */
.cta{left:0;top:2440px;width:1200px;height:442px;background:linear-gradient(90deg,#1d3f66,#3a6e9c 50%,#1d3f66)}
.cta h2{position:absolute;top:148px;width:100%;text-align:center;color:var(--white);font-size:36px;font-weight:700}
.cta .sub{position:absolute;top:205px;width:100%;text-align:center;color:var(--white);font-size:15px;font-weight:700}
.cta .btn{position:absolute;left:540px;top:258px;height:52px;display:flex;color:var(--white);font-weight:700;font-size:15px}
.cta .btn .ic{width:44px;background:var(--blue-dark);display:flex;align-items:center;justify-content:center;border-right:1px solid rgba(255,255,255,.5)}
.cta .btn .lb{background:var(--blue);padding:0 20px;line-height:52px}

/* footer */
.footer{left:0;top:2880px;width:1200px;height:445px;background:var(--footer);color:var(--white);clip-path:polygon(0 10px,50% 0,100% 10px,100% 100%,0 100%)}
.f-brand{position:absolute;left:55px;top:80px;display:flex;align-items:center;gap:10px}
.f-brand .brand-name{color:var(--blue);font-size:22px;width:220px}
.f-about{position:absolute;left:55px;top:160px;width:340px;font-size:14px;line-height:1.5}
.f-list{position:absolute;left:55px;top:225px;font-size:14px}
.f-list div{display:flex;align-items:center;gap:14px;height:40px}
.f-list .ic{width:26px;height:26px;background:#1b1b1b;display:flex;align-items:center;justify-content:center}
.f-social{position:absolute;left:55px;top:348px;display:flex;gap:5px}
.f-social span{width:30px;height:30px;background:var(--blue)}
.f-social span:nth-child(n+6){background:#1b1b1b}
.f-h{position:absolute;font-size:18px;display:flex;gap:12px;align-items:center}
.f-h:after{content:"";height:2px;background:var(--white);display:block}
.ql{left:466px;top:78px}
.ql:after{width:180px}
.art-h{left:845px;top:78px}
.art-h:after{width:115px}
.ql-list{position:absolute;left:466px;top:118px;font-size:12.5px;font-weight:700;line-height:25px;text-transform:uppercase}
.ql-list .home{text-decoration:underline}
.ql-sub{position:absolute;left:490px;top:270px;font-size:12.5px;line-height:25px;border-left:1px solid #888;padding-left:12px}
.demo{position:absolute;left:466px;top:330px;background:var(--red);border-radius:10px;font-size:10px;font-weight:700;padding:4px 10px}
.arts{position:absolute;left:845px;top:118px;width:300px}
.art{display:flex;gap:10px;margin-bottom:14px;height:72px}
.art .ph{position:relative;width:60px;height:60px;flex:none;background:linear-gradient(135deg,#c49a5a,#6b4a2a)}
.art b{display:block;font-size:12.5px;line-height:1.25}
.art span{font-size:12.5px;line-height:1.3;color:#ddd}
.copy{left:0;top:3325px;width:1200px;height:46px;background:var(--blue);color:var(--white);font-size:12.5px;text-align:center;line-height:46px}
</style>
</head>
<body>

<header>
  <div class="abs brand"><span class="brand-mark"></span><span class="brand-name">Corvandel Health Sim</span></div>
  <div class="abs top-social"><span></span><span></span><span></span><span></span></div>
  <div class="abs top-contact">
    <span>Have any questions?</span>
    <span><svg width="12" height="12" viewBox="0 0 24 24"><path fill="#333" d="M6.6 10.8a15 15 0 0 0 6.6 6.6l2.2-2.2a1 1 0 0 1 1-.25 11.4 11.4 0 0 0 3.6.57 1 1 0 0 1 1 1V20a1 1 0 0 1-1 1A17 17 0 0 1 3 4a1 1 0 0 1 1-1h3.5a1 1 0 0 1 1 1c0 1.25.2 2.45.57 3.57a1 1 0 0 1-.25 1z"/></svg>+00 415 555 0198</span>
    <span><svg width="13" height="11" viewBox="0 0 24 18"><path fill="#333" d="M0 0h24v18H0zM2 2v1l10 7 10-7V2z"/></svg>hello@corvandel.example</span>
  </div>
</header>

<nav class="abs nav">
  <ul><li class="active">Home</li><li>Benefits</li><li>Simulation</li><li>Why Virtual</li><li>Modules</li><li>Contact Us</li></ul>
  <div class="abs search">Search Here<svg width="18" height="18" viewBox="0 0 24 24"><circle cx="10" cy="10" r="7" fill="none" stroke="#111" stroke-width="2.5"/><path d="M15 15l7 7" stroke="#111" stroke-width="2.5"/></svg></div>
</nav>

<section class="abs hero" role="img" aria-label="Smiling doctor in blue scrubs with clinical staff in the background">
  <div class="abs hero-caption">
    <h1>THE BEST COACHING</h1>
    <div class="sub">To create &amp; sell online courses</div>
    <div class="rule"></div>
    <p>academia understands customers-helps them show their advantages most effective by making their website be unique</p>
  </div>
  <div class="abs dots"><span></span><span></span><span></span><span></span></div>
</section>

<section class="abs welcome">
  <h2 class="sec-title" style="display:block;margin:0;font-size:38px">Welcome to <em>Velmora Clinic</em></h2>
  <h3>We' ve built a long standing relationship based on trust</h3>
  <p>The element of interaction is of utmost importance to make the user really feel free to get involved with the virtual environment. According to Ledgerline magazine the virtual reality (VR) market is expected to grow to US$407.51 million and reach more than 25 million users by 2018. This increased demand is attributed to industries that are starting to see the potential for VR products outside of the gaming world. Education is one of these industries, especially in the STEM subjects, science, technology, engineering, and mathematics.</p>
  <h2>Our approach is holistic</h2>
  <p>The element of interaction is of utmost importance to make the user really feel free to get involved with the virtual environment. According to Ledgerline magazine the virtual reality (VR) market is expected to grow to US$407.51 million and reach more than 25 million users by 2018.</p>
  <span class="btn-start">Start Coaching</span>
</section>

<aside class="abs clinic-card">
  <div class="ph" role="img" aria-label="Virtual hospital room with a patient lying on a bed under medical equipment"></div>
  <div class="cap">What is VELMORA CLINIC<br>...and other frequently asked questions</div>
  <span class="more">MORE</span>
</aside>

<section class="abs services">
  <h2 class="sec-title">OUR SERVICES</h2>
  <div class="tag">The Backbone of our Clinic</div>
  <article class="svc" style="left:55px">
    <div class="ph" role="img" aria-label="Clinician attending to a smiling patient" style="background:linear-gradient(135deg,#f1e6df,#c9a894)"></div>
    <h4>The Patient</h4>
    <p>Corvandel Health Sim has created different patients to reflect the different sizes ders ronment.</p>
    <span class="rm">Read More</span>
  </article>
  <article class="svc" style="left:292px">
    <div class="ph" role="img" aria-label="Operating theatre with imaging equipment" style="background:linear-gradient(135deg,#e4e8ec,#8f9aa6)"></div>
    <h4>Exposure Imaging</h4>
    <p>Corvandel Health Sim has created different patients to reflect the different sizes ders ronment.</p>
    <span class="rm">Read More</span>
  </article>
  <article class="svc" style="left:530px">
    <div class="ph" role="img" aria-label="Lab researcher using a microscope" style="background:linear-gradient(135deg,#f2f4f6,#a9b6c4)"></div>
    <h4>Equipment</h4>
    <p>Corvandel Health Sim has created different patients to reflect the different sizes ders ronment.</p>
    <span class="rm">Read More</span>
  </article>
  <div class="other">
    <h3>Other Services</h3>
    <p>Personalized patient care is what sets Velmora Medical Center apart. When you visit one of our four San Francis ampus locations you can expect to receive world class care. Expert physician specialists and caring clinical staff provide you with an exceptional patient care is</p>
    <div class="rm">» Read More</div>
  </div>
</section>

<section>
  <div class="abs benefits-head">
    <h2 class="sec-title">WE GIVE BENEFITS</h2>
    <p>When it comes to special dieting, we offer specific plans</p>
  </div>
  <article class="ben" style="left:55px">
    <div class="ph" role="img" aria-label="Stack of old books with an open book on top" style="background:linear-gradient(135deg,#b58a4e,#5a3a1e)"></div>
    <h4>Benefits for Students</h4>
    <p>Students require hands on learning which encourages them to actively think learning skills for defined</p>
    <span class="rm">Read More</span>
  </article>
  <article class="ben" style="left:435px">
    <div class="ph" role="img" aria-label="Group of students studying together on grass" style="background:linear-gradient(135deg,#9fc07a,#4c7a3a)"></div>
    <h4>Benefits for Training Institute</h4>
    <p>Students require hands on learning which encourages them to actively think learning skills for defined</p>
    <span class="rm">Read More</span>
  </article>
  <article class="ben" style="left:813px">
    <div class="ph" role="img" aria-label="Doctor in white coat writing on a clipboard" style="background:linear-gradient(135deg,#eef2f4,#7aa0b8)"></div>
    <h4>Others</h4>
    <p>Students require hands on learning which encourages them to actively think learning skills for defined</p>
    <span class="rm">Read More</span>
  </article>
</section>

<section class="abs cta" role="img" aria-label="Doctor in scrubs with stethoscope and crossed arms">
  <h2>Want a coaching from us!</h2>
  <div class="sub">Call Now (600) 555-0142 and let us craft a plan together!</div>
  <div class="btn"><span class="ic"><svg width="20" height="16" viewBox="0 0 20 16"><path d="M2 8l6 6L18 2" fill="none" stroke="#fff" stroke-width="3"/></svg></span><span class="lb">Contact us Now</span></div>
</section>

<footer class="abs footer">
  <div class="f-brand"><span class="brand-mark"></span><span class="brand-name">Corvandel Health Sim</span></div>
  <p class="f-about">Premium Pressfield Theme mainly Medical Orie various layouts for any "Health &amp; Beauty" related</p>
  <div class="f-list">
    <div><span class="ic"><svg width="12" height="12" viewBox="0 0 24 24"><path fill="#fff" d="M6.6 10.8a15 15 0 0 0 6.6 6.6l2.2-2.2a1 1 0 0 1 1-.25 11.4 11.4 0 0 0 3.6.57 1 1 0 0 1 1 1V20a1 1 0 0 1-1 1A17 17 0 0 1 3 4a1 1 0 0 1 1-1h3.5a1 1 0 0 1 1 1c0 1.25.2 2.45.57 3.57a1 1 0 0 1-.25 1z"/></svg></span>(+30) 210 5550176</div>
    <div><span class="ic"><svg width="13" height="10" viewBox="0 0 24 18"><path fill="#fff" d="M0 0h24v18H0zM2 2v1l10 7 10-7V2z"/></svg></span>info@corvandel.example</div>
    <div><span class="ic"><svg width="12" height="12" viewBox="0 0 24 24"><path fill="#fff" d="M2 11L22 2l-9 20-2-9z"/></svg></span>12 Harlow Lane, Brinmoor, CA 90000</div>
  </div>
  <div class="f-social"><span></span><span></span><span></span><span></span><span></span><span></span><span></span></div>

  <h3 class="f-h ql">Quick Links</h3>
  <div class="ql-list">
    <div class="home">Home</div><div>Success Stories</div><div>Work with me</div><div>Frequently asked questions</div><div>Connect</div><div>More</div>
  </div>
  <div class="ql-sub"><div>Pricing Plans</div><div>Individual Session (Service)</div></div>
  <span class="demo">OTHER DEMOS!</span>

  <h3 class="f-h art-h">Latest Articles</h3>
  <div class="arts">
    <div class="art"><div class="ph" role="img" aria-label="Article thumbnail, healthy meal"></div><div><b>How to deal with Emotional Eating</b><span>Sed in felis velit. Quisque porta turpis vel leo accumsan...</span></div></div>
    <div class="art"><div class="ph" role="img" aria-label="Article thumbnail, healthy meal"></div><div><b>How to deal with Emotional Eating, with Emotional Eating with</b><span>It's a familiar story: You pledge to honor a daily...</span></div></div>
    <div class="art"><div class="ph" role="img" aria-label="Article thumbnail, salad dish"></div><div><b>How to deal with Emotional</b><span>INGREDIENTS For the Greek Vinaigrette 1 clove garlic 3 tablespoons...</span></div></div>
  </div>
</footer>
<div class="abs copy">© 2016 corvandelhealthsim.example Right Reserved.</div>

</body>
</html>
```